Letterhead Design Project

Need Letterhead and Envelpe design with One Single or Both Side pockets for a yong dynamic employee friendly IT services company. It should be professional and sleek and should look fresh.

Target Market(s)

IT Corporate

Industry/Entity Type

It Company

```html
<!DOCTYPE html>
<html lang="en">
<head>
<meta charset="utf-8">
<title>Kovara Technologies – Presentation Folder</title>
<link rel="stylesheet" href="https://fonts.googleapis.com/css2?family=Ubuntu:wght@400;500;700&display=swap">
<style>
  :root {
    --bg: #d9d9d9;
    --paper: #ffffff;
    --brand-red: #d42a3c;
    --brand-red-deep: #b8362a;
    --grey-mid: #8e8e8e;
    --grey-text: #6f6f6f;
    --grey-line: #e6e6e6;
  }
  * { margin: 0; padding: 0; box-sizing: border-box; }
  html, body { width: 1200px; height: 847px; overflow: hidden; }
  body {
    background: var(--bg);
    font-family: "Ubuntu", sans-serif;
    position: relative;
  }
  .folder-spread {
    position: absolute;
    left: 140px; top: 124px;
    width: 920px; height: 600px;
    display: flex;
    background: var(--paper);
  }
  .panel { position: relative; width: 460px; height: 600px; overflow: hidden; }
  .panel--back { border-right: 1px solid var(--grey-line); }

  .brand-name { color: var(--brand-red); font-weight: 700; line-height: 1; display: inline-block; text-align: center; }
  .brand-name__main { display: block; letter-spacing: 0.5px; }
  .brand-name__sub { display: block; margin-top: 1px; }

  .panel--front .brand-name { position: absolute; top: 48px; right: 58px; }
  .panel--front .brand-name__main { font-size: 34px; }
  .panel--front .brand-name__sub { font-size: 10.5px; letter-spacing: 4.4px; }

  .website {
    position: absolute; left: 160px; top: 432px;
    font-size: 11px; color: var(--grey-text); letter-spacing: 0.6px;
  }
  .website strong { color: var(--brand-red); font-weight: 700; }

  .cover-accent { position: absolute; inset: 0; }

  .panel--back .brand-name { position: absolute; left: 198px; top: 458px; }
  .panel--back .brand-name__main { font-size: 22px; }
  .panel--back .brand-name__sub { font-size: 7px; letter-spacing: 2.8px; }

  .contact-row {
    position: absolute; left: 26px; top: 512px; right: 10px;
    display: flex; gap: 16px;
    font-size: 6.4px; line-height: 1.45; color: var(--grey-text);
  }
  .contact-block { display: flex; gap: 3px; }
  .contact-block address { font-style: normal; }
  .contact-list { list-style: none; }
  .contact-list li { display: flex; align-items: center; gap: 3px; }
  .icon { width: 6px; height: 6px; flex: none; }
  .icon-square { width: 5px; height: 5px; background: var(--brand-red); flex: none; }
</style>
</head>
<body>
  <main class="folder-spread">
    <section class="panel panel--back">
      <div class="brand-name">
        <span class="brand-name__main">kovara</span>
        <span class="brand-name__sub">technologies</span>
      </div>

      <div class="contact-row">
        <div class="contact-block">
          <svg class="icon" viewBox="0 0 10 10"><path d="M5 0a3.5 3.5 0 0 0-3.5 3.5C1.5 6 5 10 5 10s3.5-4 3.5-6.5A3.5 3.5 0 0 0 5 0zm0 5a1.5 1.5 0 1 1 0-3 1.5 1.5 0 0 1 0 3z" fill="var(--brand-red)"/></svg>
          <address>Level 2, Lakeview Plaza<br>No. 112, Harbor Lane<br>Eastfield,<br>Northbridge – 40012</address>
        </div>
        <div class="contact-block">
          <svg class="icon" viewBox="0 0 10 10"><path d="M5 0a3.5 3.5 0 0 0-3.5 3.5C1.5 6 5 10 5 10s3.5-4 3.5-6.5A3.5 3.5 0 0 0 5 0zm0 5a1.5 1.5 0 1 1 0-3 1.5 1.5 0 0 1 0 3z" fill="var(--brand-red)"/></svg>
          <address>Silver Court Business Centre<br>No. 14, 3rd Floor, Maple Row,<br>2nd Phase, Westgate,<br>Northbridge 40078</address>
        </div>
        <ul class="contact-list">
          <li><svg class="icon" viewBox="0 0 10 10"><path d="M5 0a3.5 3.5 0 0 0-3.5 3.5C1.5 6 5 10 5 10s3.5-4 3.5-6.5A3.5 3.5 0 0 0 5 0zm0 5a1.5 1.5 0 1 1 0-3 1.5 1.5 0 0 1 0 3z" fill="var(--brand-red)"/></svg>232 N. Birch Avenue, Oakhaven 00231</li>
          <li><svg class="icon" viewBox="0 0 10 10"><path d="M2 0l2 2.5-1 1.5a6 6 0 0 0 3 3l1.5-1L10 8l-1.5 2C4 10 0 6 0 1.5z" fill="var(--brand-red)"/></svg>+1 555 010 2040</li>
          <li><svg class="icon" viewBox="0 0 10 10"><rect x="0" y="2" width="10" height="6" fill="var(--brand-red)"/><path d="M0 2l5 3.5L10 2" stroke="#fff" fill="none"/></svg>info@kovaratech.com</li>
          <li><svg class="icon" viewBox="0 0 10 10"><circle cx="5" cy="5" r="4.5" fill="var(--brand-red)"/></svg>www.kovaratechnologies.com</li>
        </ul>
        <ul class="contact-list">
          <li><span class="icon-square"></span>/KovaraTechnologies</li>
          <li><span class="icon-square"></span>/KovaraTech</li>
          <li><span class="icon-square"></span>@kovaratech</li>
          <li><span class="icon-square"></span>kovara.tech</li>
        </ul>
      </div>
    </section>

    <section class="panel panel--front">
      <div class="brand-name">
        <span class="brand-name__main">kovara</span>
        <span class="brand-name__sub">technologies</span>
      </div>

      <p class="website">www.<strong>kovaratechnologies</strong>.com</p>

      <svg class="cover-accent" viewBox="0 0 460 600" aria-hidden="true">
        <defs>
          <linearGradient id="accentRed" x1="0" y1="1" x2="1" y2="0">
            <stop offset="0" stop-color="#b8362a"/>
            <stop offset="1" stop-color="#d42a3c"/>
          </linearGradient>
        </defs>
        <polygon points="318,600 442,318 460,330 460,352 338,600" fill="url(#accentRed)"/>
        <polygon points="350,600 460,370 460,600" fill="#8e8e8e"/>
      </svg>
    </section>
  </main>
</body>
</html>
```